Business card and stationary for Intellectual Property Consultant & Law Firm
Harborline Claims Omniworks
Business card and stationary for Intellectual Property Consultant & Law Firm - Law
Creative Brief
Simple
Dorin Makalesu
President Director
Kelor Business Center 11th Floor Jl. Raya Wibisana Kav.37-38 Jakarta Pusat 10485, Indonesia
office@harborlineclaims.example
www.harborlineclaims.example
Member: OQRU, EKLM, UVBO, WDGF
Please add Intellectual Property Rights Consultant & Law Firm for letterhead additional of our email : hbl42@harborlineclaims.example; marks@harborlineclaims.example
please add Branch office : Surabaya (+6231) 480 3926 Medan (+6261) 819 4057 Solo (+62271) 634 918
trelvorin trelvorin
Dear All, Please provide me the stationary : letterhead, envelope, cds, ballpoint, ruler, stamps, usb sticks etc
dunmoral dunmoral
Please upload Ai or eps file of your logo thankyou
Please add : Intellectual Property Rights Consultant & Law Firm in envelope and letter head.

```html
<!DOCTYPE html>
<html lang="en">
<head>
<meta charset="utf-8">
<title>Harborline Claims Omniworks – Business Card</title>
<link href="https://fonts.googleapis.com/css2?family=Exo+2:wght@400;600&display=swap" rel="stylesheet">
<style>
  :root{
    --backdrop:#e6e6e6;
    --card:#ffffff;
    --ink:#3c3c48;
    --accent:#f0a82c;
    --band:#6e6e6e;
    --band-dark:#5f5f5f;
    --on-band:#ffffff;
  }
  *{box-sizing:border-box;margin:0;padding:0}
  html,body{width:1200px;height:948px;overflow:hidden;background:var(--backdrop);font-family:"Exo 2",sans-serif;color:var(--ink)}
  .card{position:absolute;left:290px;width:620px;height:354px;background:var(--card);border-radius:18px;overflow:hidden;box-shadow:0 6px 18px rgba(0,0,0,.12)}
  .card--front{top:64px}
  .card--back{top:500px}

  /* front */
  .brand{position:absolute;left:0;right:0;top:150px;display:flex;align-items:center;justify-content:center;gap:16px}
  .brand__mark{width:34px;height:34px;background:var(--accent)}
  .brand__name{font-size:30px;font-weight:600;color:var(--ink);letter-spacing:.5px}

  /* back */
  .contact-row{position:absolute;left:0;right:0;top:0;height:160px;display:flex}
  .contact{flex:1;display:flex;flex-direction:column;align-items:center;padding-top:22px;text-align:center}
  .contact__icon{width:44px;height:44px;border-radius:50%;background:var(--accent);display:flex;align-items:center;justify-content:center;margin-bottom:14px}
  .contact__name{font-size:20px;font-weight:600;letter-spacing:1px}
  .contact__text{font-size:14px;line-height:1.45;letter-spacing:.5px}
  .contact__role{font-size:9px;letter-spacing:1.5px;text-transform:uppercase}

  .band{position:absolute;left:0;right:0;bottom:0;height:194px;background:var(--band);color:var(--on-band);display:flex}
  .band__web{flex:0 0 290px;display:flex;flex-direction:column;align-items:center;padding-top:28px;font-size:13px;line-height:1.7;letter-spacing:.4px}
  .band__web-icon{width:44px;height:44px;border:2px solid var(--on-band);border-radius:50%;display:flex;align-items:center;justify-content:center;margin-bottom:12px}
  .band__social{flex:1;background:var(--band-dark);padding:26px 0 0 40px;display:flex;flex-direction:column;gap:14px}
  .social{display:flex;align-items:center;gap:16px;font-size:13px;letter-spacing:.4px}
  .social__dot{width:30px;height:30px;border-radius:50%;background:var(--on-band)}
</style>
</head>
<body>
  <section class="card card--front">
    <div class="brand">
      <span class="brand__mark"></span>
      <span class="brand__name">Harborline Claims Omniworks</span>
    </div>
  </section>

  <section class="card card--back">
    <div class="contact-row">
      <div class="contact">
        <span class="contact__icon">
          <svg width="22" height="22" viewBox="0 0 22 22" fill="#fff"><circle cx="11" cy="7" r="4.5"/><path d="M2.5 21c0-5 3.8-8 8.5-8s8.5 3 8.5 8z"/></svg>
        </span>
        <div class="contact__name">ARLO VENN</div>
        <div class="contact__role">Senior Designer</div>
      </div>
      <div class="contact">
        <span class="contact__icon">
          <svg width="20" height="24" viewBox="0 0 20 24"><path d="M10 1a8 8 0 0 0-8 8c0 6 8 14 8 14s8-8 8-14a8 8 0 0 0-8-8z" fill="#fff"/><circle cx="10" cy="9" r="3" fill="#f0a82c"/></svg>
        </span>
        <div class="contact__text">041 9th Floor Tower<br>Quayside Road BRK</div>
      </div>
      <div class="contact">
        <span class="contact__icon">
          <svg width="16" height="24" viewBox="0 0 16 24"><rect x="1" y="1" width="14" height="22" rx="2.5" fill="#fff"/><rect x="3.5" y="4" width="9" height="13" fill="#f0a82c"/><circle cx="8" cy="20" r="1.3" fill="#f0a82c"/></svg>
        </span>
        <div class="contact__text">014 372 5160<br>014 372 5160</div>
      </div>
    </div>

    <div class="band">
      <div class="band__web">
        <span class="band__web-icon">
          <svg width="24" height="20" viewBox="0 0 24 20" fill="none" stroke="#fff" stroke-width="2"><rect x="2" y="2" width="20" height="12" rx="1"/><path d="M9 18h6M12 14v4"/></svg>
        </span>
        <span>arlo@venndesk.example</span>
        <span>www.venndesk.example</span>
      </div>
      <div class="band__social">
        <div class="social"><span class="social__dot"></span><span>social.example/123</span></div>
        <div class="social"><span class="social__dot"></span><span>chirp.example/123</span></div>
        <div class="social"><span class="social__dot"></span><span>network.example/in/123</span></div>
      </div>
    </div>
  </section>
</body>
</html>
```